Indie publisher seeking book cover design

We are looking for ideas for a book cover for an upcoming title, 'Nana, won't you sing along as the seasons tumble by'?'

This is a story in rhyme that takes readers on a ‘then and now’ journey through time. Narrated by a grandmother, the story compares her own mother’s life and times to those of her grandchildren. Side by side vintage and full color photos compare fashion, schools, transportation, entertainment, technology, culture and the arts from the Great Depression and World War II years to those of today. A timeline of historical and current events runs throughout the book. This book creates an opportunity for readers to share their own family tree, and gives grandparents a way to start conversations about ‘who we are and where we came from’ and fulfill their role as family historian.

This is a 32 page, hardcover gift book for grandparents, packaged as a children's book. An historical timeline runs throughout, and there are black and white and full color photos on every page.

We are looking for a design that would convey the ''then and Now' theme of the book, the intergenerational-historical connections, and the lively, warmhearted verse.

Target Market(s)

This gift book for grandparents, is sold through retail book stores and speciality gift shops.

Industry/Entity Type

Events

Requirements
Must have
• Must show book title and author name, and incorporate some of the black and white, and color photos that are used in the book, or that convey the themes equally well. Must appeal to children and their families, and attract their attention.

Book is 11'x 8 1/2" landscape.
Nice to have
• Should be bright and colorful enough to appeal to children and their parents, and look like a "gift book".

See our first book, 'When the garden swing goes creaking once more..." as an example of the type of book this will be. Website is
www.whenthegardenswinggoescreakingoncemore.com
Should not have
• We are not looking for original artwork - should use real photos. Photo shop is fine.

```html
<!DOCTYPE html>
<html lang="en">
<head>
<meta charset="utf-8">
<title>Nana, won't you sing along as the seasons tumble by? — Book Cover</title>
<link rel="stylesheet" href="https://fonts.googleapis.com/css2?family=Princess+Sofia&display=swap">
<style>
  :root {
    --page-bg: #ffffff;
    --cover-paper: #dcc9a0;
    --spine-paper: #d6c296;
    --spine-edge: #c4ae80;
    --title-red: #9c2c22;
    --figure-green: #3d6449;
    --figure-green-soft: #5a7d62;
  }
  html, body {
    margin: 0;
    padding: 0;
    width: 1200px;
    height: 1000px;
    overflow: hidden;
    background: var(--page-bg);
  }
  .canvas {
    position: relative;
    width: 1200px;
    height: 1000px;
  }
  .book {
    position: absolute;
    left: 125px;
    top: 160px;
    width: 950px;
    height: 680px;
    display: flex;
    color: var(--title-red);
    font-family: "Princess Sofia", cursive;
  }

  /* Spine */
  .book-spine {
    width: 70px;
    height: 100%;
    box-sizing: border-box;
    background: var(--spine-paper);
    border-right: 2px solid var(--spine-edge);
    display: flex;
    flex-direction: column;
    align-items: center;
    padding: 24px 0;
  }
  .spine-title,
  .spine-author {
    writing-mode: vertical-rl;
    margin: 0;
    font-weight: 400;
  }
  .spine-title {
    font-size: 19px;
    line-height: 1.2;
  }
  .spine-author {
    margin-top: 40px;
    font-size: 24px;
  }

  /* Front cover */
  .book-cover {
    position: relative;
    width: 880px;
    height: 100%;
    background: var(--cover-paper);
    text-align: center;
  }
  .book-title {
    margin: 0;
    font-weight: 400;
  }
  .title-main {
    position: absolute;
    left: 0;
    right: 0;
    top: 22px;
    font-size: 120px;
    line-height: 1.1;
  }
  .title-line {
    position: absolute;
    left: 0;
    right: 0;
    line-height: 1.1;
  }
  .title-line--upper {
    top: 172px;
    font-size: 34px;
  }
  .title-line--lower {
    top: 214px;
    font-size: 44px;
  }
  .cover-art {
    position: absolute;
    left: 315px;
    top: 292px;
    width: 250px;
    height: 290px;
  }
  .author-name {
    position: absolute;
    left: 0;
    right: 0;
    top: 600px;
    margin: 0;
    font-weight: 400;
    font-size: 48px;
    line-height: 1.1;
  }
</style>
</head>
<body>
  <main class="canvas">
    <div class="book">
      <aside class="book-spine">
        <p class="spine-title">Nana, won't you sing along<br>as the seasons tumble by?</p>
        <p class="spine-author">Mara Ellison</p>
      </aside>

      <article class="book-cover">
        <h1 class="book-title">
          <span class="title-main">Nana</span>
          <span class="title-line title-line--upper">won't you sing along as the</span>
          <span class="title-line title-line--lower">seasons tumble by?</span>
        </h1>

        <svg class="cover-art" viewBox="0 0 250 290" role="img"
             aria-label="Green silhouette illustration of a small child standing, with tree roots spreading out beneath the feet">
          <defs>
            <linearGradient id="artFill" x1="0" y1="0" x2="0" y2="1">
              <stop offset="0" stop-color="var(--figure-green)"/>
              <stop offset="1" stop-color="var(--figure-green-soft)"/>
            </linearGradient>
          </defs>
          <rect x="0" y="0" width="250" height="290" rx="6" fill="url(#artFill)"/>
        </svg>

        <p class="author-name">Mara Ellison</p>
      </article>
    </div>
  </main>
</body>
</html>
```